Design a business card & stationary for a mortgage company

We are looking for a good looking business card design for our mortgage company that includes our logo. We received a free design as part of our logo project but we don't love it. The company is called "Pinecrest Mortgage Company" so we like waves and lighthouses. The logo should be included. We have a version in both vertical and horizontal that we have provided.

Industry/Entity Type

Finance

Contact Information for Business Card

This should include our new logo file

Requirements
Must have
• 3. The details you'd like on the card - name, title, phone, email, website, address, social media handles etc.
1. Marcus Hale
Vice President
732-419-6253
Fax 888-304-2918
mhale@pinecrestmortgage.example
NMLS 47162 - Company NMLS 61290
18 Larkin Ave
Toms River, NJ 08614

```html
<!DOCTYPE html>
<html lang="en">
<head>
<meta charset="utf-8">
<title>Pinecrest Mortgage Company – Business Card</title>
<link rel="stylesheet" href="https://fonts.googleapis.com/css2?family=Source+Sans+3:wght@400;600&display=swap">
<style>
  :root {
    --backdrop: #e6e8eb;
    --card: #ffffff;
    --navy: #1c5a9a;
    --sky: #2b9ad8;
    --sky-soft: #9fd0ee;
    --ink: #1f4f86;
    --band-text: #ffffff;
    --shadow: rgba(20, 30, 50, 0.18);
  }
  * { box-sizing: border-box; margin: 0; padding: 0; }
  html, body {
    width: 1200px;
    height: 900px;
    overflow: hidden;
    background: var(--backdrop);
    font-family: "Source Sans 3", "Myriad Pro", Arial, sans-serif;
  }
  .sheet {
    width: 1200px;
    height: 900px;
    display: flex;
    align-items: center;
    justify-content: center;
    gap: 48px;
  }
  .card {
    position: relative;
    width: 520px;
    height: 298px;
    background: var(--card);
    border-radius: 22px;
    overflow: hidden;
    box-shadow: 0 10px 28px var(--shadow);
  }

  /* Front */
  .card-front .brand-name {
    position: absolute;
    left: 34px;
    top: 74px;
    width: 200px;
    font-size: 27px;
    font-weight: 600;
    line-height: 1.05;
    color: var(--navy);
    letter-spacing: 0.4px;
    text-transform: uppercase;
  }
  .card-front .contact-block {
    position: absolute;
    left: 260px;
    top: 64px;
    color: var(--ink);
  }
  .person-name {
    font-size: 22px;
    font-weight: 600;
    letter-spacing: 0.6px;
    text-transform: uppercase;
    color: var(--navy);
    line-height: 1.05;
  }
  .person-title {
    font-size: 14px;
    letter-spacing: 0.5px;
    text-transform: uppercase;
    color: var(--sky);
    margin-bottom: 12px;
  }
  .contact-list { list-style: none; }
  .contact-list li {
    display: flex;
    align-items: flex-start;
    gap: 9px;
    font-size: 13.5px;
    line-height: 19px;
  }
  .contact-list .icon {
    flex: 0 0 12px;
    width: 12px;
    height: 12px;
    margin-top: 3px;
    fill: var(--sky);
  }
  .address-line { display: block; }
  .address-line + .address-line { margin-left: -21px; }
  .license-band {
    position: absolute;
    left: 0;
    right: 0;
    bottom: 0;
    height: 44px;
    background: var(--navy);
    color: var(--band-text);
    display: flex;
    align-items: center;
    padding-left: 32px;
    font-size: 13px;
    letter-spacing: 0.6px;
    text-transform: uppercase;
  }

  /* Back */
  .card-back .brand-block {
    position: absolute;
    left: 56px;
    top: 22px;
  }
  .card-back .brand-name {
    font-size: 27px;
    font-weight: 600;
    color: var(--navy);
    letter-spacing: 0.4px;
    text-transform: uppercase;
    line-height: 1.05;
  }
  .card-back .company-license {
    margin-top: 4px;
    font-size: 12px;
    letter-spacing: 3px;
    color: var(--navy);
    text-transform: uppercase;
  }
  .wave-artwork {
    position: absolute;
    left: 0;
    right: 0;
    top: 104px;
    bottom: 0;
    background: linear-gradient(160deg, var(--sky-soft) 0%, var(--sky) 45%, var(--navy) 100%);
  }
</style>
</head>
<body>
<main class="sheet">

  <section class="card card-front" aria-label="Business card front">
    <div class="brand-name">Pinecrest Mortgage Company</div>

    <div class="contact-block">
      <div class="person-name">Marcus Hale</div>
      <div class="person-title">Vice President</div>
      <ul class="contact-list">
        <li>
          <svg class="icon" viewBox="0 0 12 12" aria-hidden="true"><path d="M2.4 0.6l2 2.2-1 1.3c.8 1.6 2 2.8 3.6 3.6l1.3-1 2.2 2-1.2 2.2C4.8 10.6 1.4 7.2 0.6 1.8z"/></svg>
          <span>732-419-6253</span>
        </li>
        <li>
          <svg class="icon" viewBox="0 0 12 12" aria-hidden="true"><path d="M3 0h6v3H3zM1 4h10v5H9v3H3V9H1zM4 8v3h4V8z"/></svg>
          <span>888-304-2918</span>
        </li>
        <li>
          <svg class="icon" viewBox="0 0 12 12" aria-hidden="true"><path d="M0 2h12v1L6 7 0 3zM0 4.2l6 4 6-4V10H0z"/></svg>
          <span>mhale@pinecrestmortgage.example</span>
        </li>
        <li>
          <svg class="icon" viewBox="0 0 12 12" aria-hidden="true"><path d="M6 0a4 4 0 0 1 4 4c0 3-4 8-4 8S2 7 2 4a4 4 0 0 1 4-4zm0 2.4a1.6 1.6 0 1 0 0 3.2 1.6 1.6 0 0 0 0-3.2z"/></svg>
          <span>
            <span class="address-line">18 Larkin Ave</span>
            <span class="address-line">Toms River, NJ 08614</span>
          </span>
        </li>
      </ul>
    </div>

    <div class="license-band">NMLS 47162 - Company NMLS 61290</div>
  </section>

  <section class="card card-back" aria-label="Business card back">
    <div class="brand-block">
      <div class="brand-name">Pinecrest Mortgage Company</div>
      <div class="company-license">NMLS 61290</div>
    </div>
    <div class="wave-artwork" role="img" aria-label="Large sweeping ocean wave artwork in navy and sky blue"></div>
  </section>

</main>
</body>
</html>
```